Yoga Magazine needs 6x9 advertising flyer / postcard

I need a flyer (postcard) for my yoga magazine to hand out to businesses. The front side will serve as a WHO WE ARE, THIS IS WHAT WE DO, ETC....the back side will be ADVERTISING INFORMATION including advertising rates.

please see MS Word doc attached to this brief.

Please bleed artwork on to 6.25" x 9.25" (1/8' extra on all sides)

Target Market(s)

WOMEN ages 20-60 who practice yoga.....and some men, but mostly women.

Industry/Entity Type

Advertising

Font styles to use
Serif

Requirements
Must have
• Please find some stock photos of some nice looking, athletic people doing yoga..
Nice to have
• light and bright colors!
Should not have
• no cartoon figures

```html
<!DOCTYPE html>
<html lang="en">
<head>
<meta charset="utf-8">
<title>Lotus Leaf Magazine – Flyer</title>
<link href="https://fonts.googleapis.com/css2?family=Cinzel:wght@400;700&family=Marcellus+SC&family=Arimo:wght@400;700&family=Open+Sans:wght@400;600;700&display=swap" rel="stylesheet">
<style>
:root{
  --stage:#232323;
  --cream:#fdf3c8;
  --sand:#f7dc8f;
  --honey:#f1c04f;
  --orange:#f26a2a;
  --orange-deep:#e8501f;
  --red:#e4332a;
  --olive:#5f5632;
  --ink:#1c1c1c;
  --rule:#b7a877;
  --white:#ffffff;
}
*{box-sizing:border-box;margin:0;padding:0}
html,body{width:1200px;height:921px;overflow:hidden;background:var(--stage)}
body{position:relative;font-family:"Arimo",Arial,sans-serif;color:var(--ink)}
.page{position:absolute;top:32px;height:830px;overflow:hidden}
.page--front{left:30px;width:560px;background:linear-gradient(180deg,#fdf6d6 0%,#fbe9a9 40%,#f7cf6e 70%,#f3b848 100%)}
.page--back{left:612px;width:558px;background:linear-gradient(180deg,#fdf3cb 0%,#fbe7a6 55%,#f8d985 100%)}
.abs{position:absolute}

/* front */
.sunset-photo{position:absolute;left:0;top:405px;width:560px;height:425px;
  background:radial-gradient(ellipse at 60% 40%,rgba(255,236,160,.9),rgba(248,196,90,.6) 45%,rgba(236,160,50,.55) 80%)}
.hero-photo{position:absolute;left:290px;top:10px;width:370px;height:370px;border-radius:50%;
  border:6px solid var(--honey);background:linear-gradient(160deg,#d8ecf2 0%,#b4d2dc 40%,#e9d5c0 75%,#cfc0b5 100%)}
.inset-photo{position:absolute;left:270px;top:245px;width:112px;height:112px;border-radius:50%;
  border:4px solid var(--honey);background:linear-gradient(180deg,#f5f2ea,#dcd6c8)}
.kicker{left:23px;top:14px;font-family:"Marcellus SC",serif;font-size:23.5px;letter-spacing:2px;color:var(--olive);line-height:26px}
.headline{left:22px;top:37px;font-family:"Cinzel",serif;font-weight:700;font-size:33px;color:var(--red);letter-spacing:.5px}
.kicker--end{top:78px}
.section-title{font-family:"Cinzel",serif;font-weight:700;font-size:15.5px;letter-spacing:.6px;color:var(--ink)}
.meaning{left:28px;top:143px;width:268px;font-size:11.2px;line-height:15px;text-align:justify}
.title-band{left:0;top:351px;width:560px;height:54px;background:linear-gradient(90deg,var(--orange-deep),var(--orange) 60%,#f5893a);
  color:var(--white);font-family:"Cinzel",serif;font-size:30px;letter-spacing:1px;text-align:center;line-height:54px}
.checklist{list-style:none;font-size:12.4px;line-height:16.3px}
.checklist li{padding-left:14px;position:relative}
.checklist li::before{content:"";position:absolute;left:1px;top:4px;width:7px;height:4px;border-left:2px solid var(--ink);border-bottom:2px solid var(--ink);transform:rotate(-45deg)}
.body-copy{font-size:12.4px;line-height:14.4px;text-align:justify}
.contact-card{left:300px;top:729px;width:240px;height:90px;border:1px solid #e2b840;border-radius:3px;
  background:linear-gradient(180deg,#f8d352,#f2bc38);text-align:center;font-family:"Open Sans",sans-serif;font-size:12.4px;line-height:19px;padding-top:6px}

/* back */
.ad-title{left:34px;top:18px;font-family:"Open Sans",sans-serif;font-weight:700;font-size:18px;letter-spacing:.4px}
.ad-title span{font-weight:400;font-size:15.5px}
.rates{position:absolute;left:8px;top:55px;width:540px;border-collapse:collapse;font-size:11.4px}
.rates th{background:var(--orange);color:var(--white);font-family:"Open Sans",sans-serif;font-weight:400;font-size:12.4px;height:36px;border:1px solid #f6a56e}
.rates th:first-child{text-align:left;padding-left:6px;font-weight:700;font-size:13px}
.rates td{height:33.4px;border:1px solid var(--rule);text-align:center;background:rgba(255,250,225,.35)}
.rates td:first-child{text-align:left;padding-left:6px}
.box{position:absolute;border:1px solid var(--rule)}
.surcharge{left:8px;top:366px;width:540px;height:38px;font-size:10.8px;padding:11px 10px}
.directories{left:8px;top:404px;width:540px;height:149px;padding:10px 10px}
.photo-pose{position:absolute;right:0;top:0;width:230px;height:148px;background:linear-gradient(180deg,rgba(255,250,230,0) 0%,rgba(228,224,212,.7) 60%,rgba(200,196,188,.8) 100%)}
.dir-head{font-weight:700;font-size:12.2px;margin-bottom:3px}
.bullets{list-style:none;font-size:11.2px;line-height:18px;padding-left:8px}
.bullets li::before{content:"•";margin-right:7px}
.specs{left:8px;top:565px;width:248px;height:246px;padding:8px 8px;font-size:9.6px;line-height:13.4px}
.specs h3{font-size:12.4px;margin-bottom:5px}
.specs p{margin-bottom:5px}
.promise{left:278px;top:565px;width:270px;height:102px;background:linear-gradient(90deg,var(--orange-deep),#f38a48);color:var(--white);padding:6px 14px}
.promise h3{font-family:"Cinzel",serif;font-weight:400;font-size:17px;letter-spacing:1px;margin-bottom:4px}
.promise p{font-size:11.2px;line-height:13.8px;text-align:justify}
.ad-contact{left:280px;top:678px;width:266px;height:128px;border:1px solid #e2b840;border-radius:3px;background:linear-gradient(180deg,#f6cd4c,#f0b733);padding:8px 14px;font-size:12.4px;line-height:17.4px}
.ad-contact h3{font-size:12.8px;margin-bottom:6px}
</style>
</head>
<body>

<section class="page page--front">
  <div class="sunset-photo" role="img" aria-label="Photo: woman in a yoga pose silhouetted against a sunset on the beach"></div>
  <div class="hero-photo" role="img" aria-label="Photo: woman in pink top doing a seated yoga stretch by the sea"></div>
  <div class="inset-photo" role="img" aria-label="Photo: man in a kneeling yoga stretch"></div>

  <div class="abs kicker">San Diego’s First Free</div>
  <div class="abs headline">YOGA MAGAZINE</div>
  <div class="abs kicker kicker--end">Is Here!!!</div>

  <h2 class="abs section-title" style="left:23px;top:115px">The Meaning of Namaste:</h2>
  <p class="abs meaning">‘Namaste’ or ‘namaskar’ is the Hindu way of greeting and saying goodbye to people. It is not a superficial gesture or a mere word...it is deeper and is for all people - young and old, friends and strangers. You’ll often hear it spoken in combination with a slight bow and the Anjali Mudra – the placement of the hands together pulled close to the heart in a fashion similar to a prayer pose. In Sanskrit, the word ‘namah’ means BOW, ‘as’ means I, and ‘te’ means YOU, translating roughly into “I bow to you,” or "I bow to the good (godly) qualities in you."</p>

  <div class="abs title-band">Lotus Leaf Magazine</div>

  <h2 class="abs section-title" style="left:28px;top:418px">Where We Can Be Found:</h2>
  <ul class="abs checklist" style="left:30px;top:442px">
    <li>Yoga studios</li><li>Gyms / Fitness Facilities</li><li>Health Food Stores</li><li>Restaurants</li>
    <li>Natural Grocery Markets</li><li>Massage Therapists and Acupuncturists</li>
    <li>Chiropractor’s, Doctor’s &amp; Dentist’s offices</li><li>Veterinarians</li><li>Real Estate Office Lobbies</li>
  </ul>

  <h2 class="abs section-title" style="left:28px;top:599px">Distribution Areas:</h2>
  <ul class="abs checklist" style="left:30px;top:623px">
    <li>Carlsbad</li><li>Encinitas</li><li>Solana Beach</li><li>Del Mar</li><li>Carmel Valley</li><li>UTC</li>
    <li>La Jolla</li><li>Pacific Beach</li><li>Mission Valley (Winter 2015)</li><li>North Park (Winter 2015)</li>
    <li>Hillcrest (Winter 2015)</li><li>Balboa Park (Winter 2015)</li>
  </ul>

  <h2 class="abs section-title" style="left:297px;top:418px">Who We Are:</h2>
  <p class="abs body-copy" style="left:300px;top:439px;width:240px">Lotus Leaf Magazine is San Diego's original yoga magazine! We are a free magazine that is distributed every other month throughout San Diego. We have articles on yoga, health, family, nutrition, pets, fitness, recipes and other inspirational topics. In every issue, we have an "events" section dedicated to upcoming community gatherings, a section for astrology, and also a community</p>

  <h2 class="abs section-title" style="left:297px;top:597px">Locally Focused:</h2>
  <p class="abs body-copy" style="left:300px;top:619px;width:240px">Our magazine is published with a local focus, which means that almost all the events and advertisers are from the San Diego area. Our articles are predominantly written by local writers, with the occasional national personality thrown in for fresh perspective. Support LOCAL!</p>

  <div class="abs contact-card">Dana Reyes<br>Lotus Leaf Magazine - Publisher<br>hello@lotusleafmagsd.com<br>858-555-0142</div>
</section>

<section class="page page--back">
  <h1 class="abs ad-title">ADVERTISING INFORMATION <span>(All rates listed are per issue)</span></h1>

  <table class="rates">
    <thead><tr><th style="width:213px">All rates listed are per issue.</th><th>One Issue</th><th>Two Issue</th><th>Three Issue</th><th>Four Issue</th></tr></thead>
    <tbody>
      <tr><td>Business Card (3.5”w x 2”h)</td><td>$110</td><td>$100</td><td>$90</td><td>$75</td></tr>
      <tr><td>1/4 Page (3.8”w x 5”h)</td><td>$225</td><td>$210</td><td>$195</td><td>$180</td></tr>
      <tr><td>1/2 Page Horizontal (5”w x 7.75”h)</td><td>$450</td><td>$420</td><td>$390</td><td>$360</td></tr>
      <tr><td>1/2 Page Vertical (3.8”w x 10.25”h)</td><td>$450</td><td>$420</td><td>$390</td><td>$360</td></tr>
      <tr><td>Full Page (8.5”w x 11”h)</td><td>$800</td><td>$750</td><td>$725</td><td>$700</td></tr>
      <tr><td>Page 3 (8.5”w x 11”h)</td><td>$1,500</td><td>$1,425</td><td>$1,350</td><td>$1,275</td></tr>
      <tr><td>Inside Cover (8.5”w x 11”h)</td><td>$1,225</td><td>$1,150</td><td>$1,075</td><td>$1,000</td></tr>
      <tr><td>Back Cover (8.5”w x 11”h)</td><td>$2,250</td><td>$2,200</td><td>$2,150</td><td>$2,100</td></tr>
    </tbody>
  </table>

  <div class="box surcharge"><b>Color Surcharge:</b>&nbsp; Full Page add $100; Half Page add $85; ¼ page add $65; Business Card add $35</div>

  <div class="box directories">
    <div class="photo-pose" role="img" aria-label="Photo: woman in a standing yoga pose on rocks by the water"></div>
    <div class="dir-head" style="position:relative">Directories:&nbsp; Holistic, Restaurant, Green Business and Yoga Related</div>
    <ul class="bullets" style="position:relative">
      <li>65 Spaces per line, 1 line, FOUR ISSUES for $80</li>
      <li>65 Spaces per line, 2 lines, FOUR ISSUES for $150</li>
      <li>65 Spaces per line, 3 lines, FOUR ISSUES for $225</li>
    </ul>
    <div class="dir-head" style="position:relative;margin-top:14px">Event Listings:</div>
    <ul class="bullets" style="position:relative"><li>50 words for $15 (50 word maximum)</li></ul>
  </div>

  <div class="box specs">
    <h3>Ad Specs:</h3>
    <p>• Final trim size: 8.5”x11”.</p>
    <p>• Please keep text 0.125” away from edges</p>
    <p>• Full-page ad size: 8.25”x10.5” for non-bleeds;<br>&nbsp; 8.625”x11.25” for bleeds.</p>
    <p>• Please inquire about specs for other print<br>&nbsp; and digital edition positions</p>
    <p>• Binding: Saddle stitch</p>
    <p>• Stock and inks: Artwork colors should be CMYK;<br>&nbsp; artwork with PMS colors, metallic colors and<br>&nbsp; spot varnish will not be accepted</p>
    <p>• Advertiser must provide logo and artwork as<br>&nbsp; press-quality JPG, EPS, TIF or PDF files</p>
  </div>

  <div class="abs promise">
    <h3>OUR PROMISE:</h3>
    <p>With our dedication to the community and you, we promise to continually bring top quality, trustworthy and local sources of information to the pages of Lotus Leaf Magazine.</p>
  </div>

  <div class="abs ad-contact">
    <h3>AD QUESTIONS or ARTWORK:</h3>
    Dana Reyes<br>Lotus Leaf Magazine<br>Publisher<br>hello@lotusleafmagsd.com<br>858-555-0142
  </div>
</section>

</body>
</html>
```